Corbin Haskell International Country Singer

We need a Cd cover for Corbin Haskell. The title is "Ride The Dawn". Really looking for a fresh innovative look at days gone by. Fairly standard brief as far as cd cover's are concerned. looking for a catchy flow through the booklet. Images are available of the artist, more for inside the booklet than for use on the cover.
New CD title: Ride The Dawn
Artist name: Corbin Haskell
Current website: CorbinHaskell.example
Facebook: fanpage.example/CorbinHaskell

Industry/Entity Type

Singer

Logo Text

Corbin Haskell Ride The Dawn

Font styles to use
Decorative

```html
<!DOCTYPE html>
<html lang="en">
<head>
<meta charset="utf-8">
<title>Corbin Haskell – Ride The Dawn</title>
<link rel="stylesheet" href="https://fonts.googleapis.com/css2?family=Cinzel:wght@400;600;700&family=Cormorant+Garamond:ital,wght@1,600&display=swap">
<style>
  :root {
    --backdrop: #1a1a1a;
    --green-bright: #22924a;
    --green-mid: #167a3a;
    --green-deep: #0b3e1e;
    --band-red: #d8262b;
    --title-cream: #e8e4dc;
    --accent-red: #c8161c;
    --rule-cream: #d9d4ca;
    --ink-white: #f4f1ea;
  }
  html, body {
    margin: 0;
    width: 1200px;
    height: 829px;
    overflow: hidden;
    background: var(--backdrop);
  }
  .cover {
    position: absolute;
    left: 235px;
    top: 45px;
    width: 739px;
    height: 739px;
    overflow: hidden;
    background:
      radial-gradient(ellipse at 30% 35%, rgba(255,255,255,0.08), transparent 55%),
      radial-gradient(ellipse at 85% 15%, var(--green-deep), transparent 45%),
      radial-gradient(ellipse at 10% 90%, var(--green-deep), transparent 50%),
      radial-gradient(ellipse at 90% 85%, rgba(6,40,18,0.9), transparent 45%),
      linear-gradient(160deg, var(--green-bright), var(--green-mid) 55%, var(--green-deep));
  }
  .artist-band {
    position: absolute;
    left: 0;
    top: 150px;
    width: 100%;
    height: 42px;
    background: var(--band-red);
  }
  .artist-name {
    position: absolute;
    left: 38px;
    top: 5px;
    margin: 0;
    font-family: "Cinzel", serif;
    font-weight: 700;
    font-size: 27px;
    letter-spacing: 1px;
    color: var(--ink-white);
  }
  .ornament {
    position: absolute;
    background: radial-gradient(ellipse, rgba(8,50,22,0.55), transparent 70%);
  }
  .ornament-left { left: 60px; top: 220px; width: 190px; height: 140px; }
  .ornament-right { left: 330px; top: 240px; width: 390px; height: 230px; }
  .guitar {
    position: absolute;
    left: 120px;
    top: 470px;
    width: 90px;
    height: 210px;
    background: radial-gradient(ellipse at 50% 65%, rgba(5,30,14,0.75), transparent 70%);
  }
  .title-rule {
    position: absolute;
    height: 3px;
    background: var(--rule-cream);
  }
  .rule-top { left: 100px; top: 398px; width: 420px; }
  .rule-bottom { left: 70px; top: 628px; width: 450px; }
  .album-title {
    position: absolute;
    left: 95px;
    top: 400px;
    margin: 0;
    font-family: "Cinzel", serif;
    font-weight: 400;
    color: var(--title-cream);
    line-height: 1;
  }
  .title-line {
    display: block;
    font-size: 104px;
    letter-spacing: -2px;
  }
  .title-line + .title-line { margin-top: 8px; }
  .title-small {
    font-family: "Cormorant Garamond", serif;
    font-style: italic;
    font-weight: 600;
    font-size: 46px;
    color: var(--accent-red);
    vertical-align: 42px;
    letter-spacing: 0;
    margin-left: 4px;
  }
  .contact {
    position: absolute;
    left: 180px;
    top: 648px;
    margin: 0;
    font-family: "Cinzel", serif;
    font-weight: 600;
    font-size: 16px;
    line-height: 1.35;
    color: var(--ink-white);
  }
</style>
</head>
<body>
  <main class="cover">
    <div class="ornament ornament-left" role="img" aria-label="Faint baroque scroll ornament"></div>
    <div class="ornament ornament-right" role="img" aria-label="Faint baroque acanthus ornament"></div>
    <div class="artist-band">
      <p class="artist-name">Corbin Haskell</p>
    </div>
    <div class="guitar" role="img" aria-label="Dark silhouette of an acoustic guitar"></div>
    <div class="title-rule rule-top"></div>
    <h1 class="album-title">
      <span class="title-line">RIDE<span class="title-small">the</span></span>
      <span class="title-line">DAWN</span>
    </h1>
    <div class="title-rule rule-bottom"></div>
    <p class="contact">CorbinHaskell.example<br>fanpage.example/CorbinHaskell</p>
  </main>
</body>
</html>
```